lab equipment website

We need a fresh new look for a company website called tarvio. We will be using the current logo and brand colors on their current website tarvio.com. They want to keep their text and on-page SEO, but would like to reformat it to look more modern and fresh. They want to have everything be high performance with a great user experience. Their main call to action is for people to fill in a contact form so they can call them. There is some information that is purposely above the fold on the instrument pages. I will need the home page, about page and a leasing page.

```html
<!DOCTYPE html>
<html lang="en">
<head>
<meta charset="utf-8">
<title>tarvio – Lab Equipment Service Plans and Leasing</title>
<link href="https://fonts.googleapis.com/css2?family=Poppins:wght@300;400;500;600;700&display=swap" rel="stylesheet">
<style>
:root{
  --teal:#17a392;
  --teal-dark:#2b7d74;
  --teal-deep:#1f4d52;
  --blue:#2a9ad6;
  --navy:#1c3556;
  --green-light:#93d19a;
  --ink:#444;
  --body:#777;
  --black:#0d0d0d;
  --footer:#141414;
  --white:#fff;
}
*{box-sizing:border-box;margin:0;padding:0}
html,body{width:1200px;height:3203px;overflow:hidden}
body{position:relative;font-family:'Poppins',sans-serif;color:var(--ink);background:var(--white)}
.abs{position:absolute}
/* top bar */
.topbar{left:0;top:0;width:1200px;height:32px;background:var(--black)}
.topbar .contact{left:715px;top:0;width:485px;height:32px;background:var(--teal-dark);display:flex;align-items:center;font-size:13px;color:var(--white);letter-spacing:.5px}
.contact .ico{width:44px;height:32px;background:rgba(255,255,255,.18);display:flex;align-items:center;justify-content:center;margin-right:14px}
.contact span.txt{margin-right:90px}
/* header */
.header{left:0;top:32px;width:1200px;height:118px;background:var(--black)}
.brand{display:flex;align-items:center;gap:10px;color:var(--white);font-weight:700;font-size:34px;letter-spacing:-.5px}
.brand .mark{width:34px;height:34px;background:var(--teal);border-radius:4px}
.header .brand{left:122px;top:30px}
.nav{left:0;top:46px;width:1200px;height:20px;font-size:14px;font-weight:500;color:var(--white);letter-spacing:1px}
.nav a{position:absolute;top:0;color:inherit;text-decoration:none;white-space:nowrap}
.nav a.active{color:var(--teal)}
/* hero */
.hero{left:0;top:150px;width:1200px;height:294px;background:linear-gradient(90deg,#e4e4e4,#f3f3f3 60%,#fafafa)}
.hero .kicker{left:122px;top:34px;font-size:22px;font-weight:600;color:var(--teal)}
.hero h1{left:122px;top:62px;font-size:33px;font-weight:700;color:var(--blue);letter-spacing:-.3px}
.hero p{left:122px;top:116px;width:420px;font-size:13.5px;line-height:22px;color:#8a8a8a}
.btn{display:flex;align-items:center;background:var(--teal);color:var(--white);font-size:13px;font-weight:500;letter-spacing:1px;height:38px}
.btn .cap{width:44px;height:38px;background:var(--teal-dark);margin-right:24px;display:flex;align-items:center;justify-content:center}
.hero .btn{left:122px;top:212px;width:177px}
.hero .product{left:630px;top:0;width:570px;height:294px;background:radial-gradient(ellipse at 55% 50%,#d6dbe0 0%,#e9ecef 45%,rgba(250,250,250,0) 75%)}
.marker{left:556px;top:416px;width:54px;height:80px}
/* intro */
.section-title{left:0;width:1200px;text-align:center;font-size:27px;font-weight:600;color:#4a4a4a;line-height:42px}
.intro-title{top:530px}
.intro-text{left:235px;top:622px;width:730px;text-align:center;font-size:14px;line-height:27px;color:var(--body)}
.features{left:218px;top:775px;display:flex}
.feature{display:flex;align-items:center;font-size:12px;line-height:18px;color:var(--teal-dark);font-weight:500}
.feature .dot{width:64px;height:64px;border-radius:50%;background:var(--teal);flex:none;margin-right:18px;display:flex;align-items:center;justify-content:center;box-shadow:0 3px 8px rgba(0,0,0,.12)}
/* understand */
.needs-title{top:936px}
.diagram-bg{left:0;top:1046px;width:1200px;height:491px;background:linear-gradient(180deg,#fff 0%,#eef8f8 55%,#e6f4f5 100%)}
.diagram{left:0;top:1046px;width:1200px;height:570px}
.needs-text{left:235px;top:1648px;width:730px;text-align:center;font-size:14px;line-height:27px;color:var(--body)}
.benefits{left:260px;top:1752px;width:700px;list-style:none}
.benefits li{position:relative;padding-left:54px;font-size:15px;font-weight:500;line-height:26px;color:#4d4d4d;margin-bottom:14px}
.benefits li::before{content:"";position:absolute;left:3px;top:7px;width:13px;height:13px;border-radius:50%;background:var(--teal-dark)}
.closing{left:235px;top:2090px;width:730px;font-size:14px;line-height:27px;color:var(--body)}
/* team */
.team{left:0;top:2220px;width:1200px;height:466px;background:linear-gradient(135deg,#e7e7e7,#f1f1f1 50%,#e4e4e4)}
.team-title{top:2260px}
.card{top:2398px;width:277px;height:224px;background:var(--white);box-shadow:0 4px 14px rgba(0,0,0,.06);text-align:center}
.card .avatar{position:absolute;left:96px;top:-42px;width:85px;height:85px;border-radius:50%;border:4px solid var(--white);box-shadow:0 2px 8px rgba(0,0,0,.15)}
.card h3{margin-top:80px;font-size:18px;font-weight:600;color:#222;letter-spacing:.5px}
.card .role{margin-top:4px;font-size:14px;color:#555;letter-spacing:1px}
.card hr{border:0;border-top:1px solid #e2e2e2;margin:28px 22px 18px}
.card .social{display:flex;justify-content:center;gap:16px}
.card .social i{width:7px;height:7px;border-radius:50%;background:#333;display:block}
/* footer */
.footer{left:0;top:2750px;width:1200px;height:453px;background:var(--footer)}
.footer-band{left:0;top:271px;width:1200px;height:182px;background:#0a0a0a}
.cta{left:175px;top:2707px;width:852px;height:107px;background:var(--teal-deep);padding:18px 0 0 24px;color:var(--white)}
.cta h4{font-size:18px;font-weight:600;color:var(--teal)}
.cta p{font-size:13.5px;line-height:23px;margin-top:4px}
.cta p em{font-style:normal;color:var(--teal)}
.cta .btn{position:absolute;left:632px;top:37px;width:175px}
.footer .brand{left:199px;top:160px;font-size:28px}
.footer .brand .mark{width:28px;height:28px}
.about-blurb{left:199px;top:233px;width:165px;font-size:10px;line-height:20px;color:#aaa}
.fcol{top:168px;font-size:10.5px;color:#aaa}
.fcol h5{font-size:12px;font-weight:500;color:var(--white);letter-spacing:1px;padding-bottom:8px;border-bottom:1px solid #333;position:relative;margin-bottom:22px}
.fcol h5::after{content:"";position:absolute;left:0;bottom:-1px;width:36px;height:2px;background:var(--teal)}
.fcol .cols{display:flex;gap:38px;line-height:20px}
.fcol a{color:inherit;text-decoration:none;display:block}
.fcol a.on{color:var(--teal)}
.email{margin-top:14px;width:175px;height:24px;border:1px solid #555;display:flex;align-items:center;justify-content:space-between;padding:0 8px;font-size:10px;color:#888}
.copy{left:199px;top:418px;font-size:10px;color:#bbb}
.fsocial{left:858px;top:420px;display:flex;gap:22px}
.fsocial i{width:8px;height:8px;border-radius:50%;background:#bbb;display:block}
.totop{left:572px;top:3184px;width:22px;height:19px;background:var(--teal);display:flex;align-items:center;justify-content:center}
</style>
</head>
<body>

<div class="abs topbar">
  <div class="abs contact">
    <div class="ico"><svg width="14" height="14" viewBox="0 0 24 24"><path fill="#fff" d="M6.6 10.8a15 15 0 0 0 6.6 6.6l2.2-2.2c.3-.3.7-.4 1-.2 1.1.4 2.3.6 3.6.6.6 0 1 .4 1 1V20c0 .6-.4 1-1 1A17 17 0 0 1 3 4c0-.6.4-1 1-1h3.5c.6 0 1 .4 1 1 0 1.3.2 2.5.6 3.6.1.3 0 .7-.2 1z"/></svg></div>
    <span class="txt">(415) 555-0148</span>
    <div class="ico"><svg width="16" height="12" viewBox="0 0 16 12"><rect x="0.5" y="0.5" width="15" height="11" fill="#fff"/><path d="M1 1l7 6 7-6" stroke="#2b7d74" fill="none"/></svg></div>
    <span>info@tarvio.com</span>
  </div>
</div>

<header class="abs header">
  <div class="abs brand"><span class="mark"></span>tarvio</div>
  <nav class="abs nav">
    <a class="active" href="#" style="left:576px">HOME</a>
    <a href="#" style="left:684px">ABOUT</a>
    <a href="#" style="left:798px">LEASING</a>
    <a href="#" style="left:924px">FAQ</a>
    <a href="#" style="left:1019px">CONTACT</a>
  </nav>
</header>

<section class="abs hero">
  <div class="abs product" role="img" aria-label="Benchtop laboratory instrument with a blue lid"></div>
  <div class="abs kicker">Our goal is simple:</div>
  <h1 class="abs">save labs time and money</h1>
  <p class="abs">tarvio is a lab support program that provides scientists with comprehensive maintenance/repair coverage and operating lease solutions at an affordable price.</p>
  <div class="abs btn"><span class="cap"><svg width="14" height="14" viewBox="0 0 14 14"><path d="M4 2l6 5-6 5" stroke="#fff" stroke-width="2" fill="none"/></svg></span>LEARN MORE</div>
</section>

<svg class="abs marker" viewBox="0 0 54 80" aria-hidden="true">
  <rect x="0" y="0" width="54" height="58" fill="#fff"/>
  <circle cx="27" cy="32" r="13" fill="#17a392"/>
  <path d="M16 58h22l-11 14z" fill="#17a392"/>
</svg>

<h2 class="abs section-title intro-title">Trusted Company Offering<br>Scientific Equipment Service Plans and Flexible Leases</h2>
<p class="abs intro-text">At tarvio, our goal is to ensure the success of your business. Whether you are running a laboratory or other scientific facilities, we want to keep you provided with the best in cutting-edge equipment. That's why we offer flexible scientific equipment leasing options with worry-free service plans- to provide your business with the tools needed to perform at its peak.</p>

<div class="abs features">
  <div class="feature" style="width:271px"><span class="dot"><svg width="26" height="26" viewBox="0 0 26 26"><rect x="3" y="7" width="20" height="15" rx="2" fill="none" stroke="#fff" stroke-width="2"/><path d="M13 10v9M8.5 14.5h9" stroke="#fff" stroke-width="2"/></svg></span>Worry free lab equipment<br>PM/repair coverage.</div>
  <div class="feature" style="width:299px"><span class="dot"><svg width="26" height="26" viewBox="0 0 26 26"><path d="M5 14l5 5 11-12" stroke="#fff" stroke-width="2.4" fill="none"/></svg></span>Cost-effective lease<br>structures and payment plans.</div>
  <div class="feature" style="width:260px"><span class="dot"><svg width="26" height="26" viewBox="0 0 26 26"><path d="M10 3h6M11 3v7l-6 11h16l-6-11V3" stroke="#fff" stroke-width="2" fill="none"/></svg></span>Knowledge of the<br>laboratory.</div>
</div>

<h2 class="abs section-title needs-title">We Understand Your Needs Because<br>We Are Scientists First</h2>
<div class="abs diagram-bg"></div>

<svg class="abs diagram" viewBox="0 0 1200 570" aria-label="Five service benefits around a central promise: we have you completely covered">
  <defs>
    <radialGradient id="coverGlow" cx="50%" cy="50%" r="50%">
      <stop offset="0" stop-color="#1c3556"/>
      <stop offset="0.55" stop-color="#2b7d74"/>
      <stop offset="1" stop-color="#93d19a"/>
    </radialGradient>
  </defs>
  <circle cx="566" cy="370" r="194" fill="#fff"/>
  <circle cx="566" cy="370" r="184" fill="url(#coverGlow)" role="img" aria-label="Concentric ring graphic in green, teal and navy"/>
  <text x="566" y="362" text-anchor="middle" font-family="Poppins, sans-serif" font-size="13" font-weight="600" fill="#fff">We have</text>
  <text x="566" y="380" text-anchor="middle" font-family="Poppins, sans-serif" font-size="13" font-weight="600" fill="#fff">you completely</text>
  <text x="566" y="398" text-anchor="middle" font-family="Poppins, sans-serif" font-size="13" font-weight="600" fill="#fff">covered</text>

  <g stroke="#2b7d74" stroke-width="2">
    <line x1="568" y1="162" x2="568" y2="216"/>
    <line x1="400" y1="226" x2="446" y2="262"/>
    <line x1="752" y1="226" x2="706" y2="262"/>
    <line x1="340" y1="335" x2="392" y2="357"/>
    <line x1="808" y1="335" x2="756" y2="357"/>
  </g>
  <g fill="#1c3556">
    <circle cx="568" cy="216" r="10"/><circle cx="446" cy="262" r="10"/><circle cx="706" cy="262" r="10"/><circle cx="392" cy="357" r="10"/><circle cx="756" cy="357" r="10"/>
  </g>
  <g fill="#2b7d74" stroke="#fff" stroke-width="4">
    <circle cx="568" cy="124" r="40"/><circle cx="374" cy="199" r="40"/><circle cx="777" cy="197" r="40"/><circle cx="303" cy="329" r="40"/><circle cx="845" cy="329" r="40"/>
  </g>
  <g stroke="#fff" stroke-width="3" fill="none" stroke-linecap="round">
    <path d="M555 130v-8a13 13 0 0 1 26 0v8"/><rect x="551" y="126" width="7" height="12" fill="#fff"/><rect x="578" y="126" width="7" height="12" fill="#fff"/>
    <path d="M362 199a8 8 0 0 1 12-8l4 4M386 199a8 8 0 0 1-12 8l-4-4"/>
    <path d="M765 198l9 9 16-18"/>
    <path d="M288 338h10l10-6h8M296 322l10-8 8 8-10 8z"/>
    <path d="M835 318c0 14 8 22 22 22l3-6-6-4-4 3c-4-2-7-5-9-9l3-4-4-6z"/>
  </g>
  <g font-family="Poppins, sans-serif" font-size="13.5" fill="#555">
    <text x="568" y="63" text-anchor="middle">Customer Service</text>
    <text x="296" y="191" text-anchor="end">Lease Plan Flexibility</text>
    <text x="848" y="191">Reliability</text>
    <text x="246" y="328" text-anchor="end">Cost Saving</text>
    <text x="912" y="328">Continued Support</text>
  </g>
</svg>

<p class="abs needs-text">When it comes to creating innovative solutions that cater to your lab, tarvio's dedicated team of problem-solvers has got you covered. Here's how we save you time and money:</p>

<ul class="abs benefits">
  <li>We collaborate with you directly– no middlemen</li>
  <li>We handle scientific equipment service, repairs, and maintenance</li>
  <li>We consolidate and streamline the ancillary work associated with lab equipment procurement and service</li>
  <li>We utilize our networks to bring you the most cost-savings possible</li>
  <li>We improve cash flow by removing the upfront cost of purchasing, freeing up capital in your everyday budget</li>
  <li>We may provide tax advantages with our lease structures</li>
</ul>

<p class="abs closing">We regularly provide businesses with what they need to improve their budget and efficiency. We offer laboratory equipment leasing for a wide range of needs. If you want to discuss your needs more in-depth, don't hesitate to call us at (415) 555-0148 or fill out our contact form.</p>

<section class="abs team"></section>
<h2 class="abs section-title team-title">Our Team</h2>
<div class="abs card" style="left:171px">
  <div class="avatar" role="img" aria-label="Portrait photo of Evan Lio" style="background:#8a6a55"></div>
  <h3>EVAN LIO</h3><div class="role">LAB RELATIONS</div><hr>
  <div class="social"><i></i><i></i><i></i><i></i></div>
</div>
<div class="abs card" style="left:461px">
  <div class="avatar" role="img" aria-label="Portrait photo of Mark Delaney" style="background:#b9a497"></div>
  <h3>MARK DELANEY</h3><div class="role">FINANCE</div><hr>
  <div class="social"><i></i><i></i><i></i><i></i></div>
</div>
<div class="abs card" style="left:754px">
  <div class="avatar" role="img" aria-label="Portrait photo of Ravi Sandhu" style="background:#9b6a4a"></div>
  <h3>RAVI SANDHU</h3><div class="role">OPERATIONS</div><hr>
  <div class="social"><i></i><i></i><i></i><i></i></div>
</div>

<footer class="abs footer">
  <div class="abs footer-band"></div>
  <div class="abs brand"><span class="mark"></span>tarvio</div>
  <p class="abs about-blurb">Lorem Ipsum is simply dummy text of the printing and typesetting industry. Lorem Ipsum has been the industry's standard dummy</p>
  <div class="abs fcol" style="left:395px;width:175px">
    <h5>SITEMAP</h5>
    <div class="cols"><div><a href="#">Services</a><a class="on" href="#">About Us</a><a href="#">Our Team</a><a href="#">Portfolio</a></div><div><a href="#">Blog</a><a href="#">Testimonial</a><a href="#">Contact Us</a></div></div>
  </div>
  <div class="abs fcol" style="left:591px;width:175px">
    <h5>ACHIVES</h5>
    <div class="cols"><div><a href="#">January 2015</a><a href="#">February 2015</a><a href="#">March 2015</a><a href="#">April 2015</a></div><div><a href="#">May 2015</a><a href="#">June 2015</a><a href="#">July 2015</a></div></div>
  </div>
  <div class="abs fcol" style="left:788px;width:175px">
    <h5>NEWSLETTER</h5>
    <div style="line-height:18px">Sign up for our mailing list to get latest updates and offers</div>
    <div class="email"><span>Email address</span><span>→</span></div>
  </div>
  <div class="abs copy">Copyright © 2019 . All rights reserved.</div>
  <div class="abs fsocial"><i></i><i></i><i></i><i></i></div>
</footer>

<div class="abs cta">
  <h4>Further questions?</h4>
  <p>Feel free to contact us if you have any questions or comments.<br>We promise to get back to you <em>within 24 hours.</em></p>
  <div class="btn"><span class="cap"><svg width="14" height="14" viewBox="0 0 14 14"><path d="M4 2l6 5-6 5" stroke="#fff" stroke-width="2" fill="none"/></svg></span>LEARN MORE</div>
</div>

<div class="abs totop"><svg width="10" height="8" viewBox="0 0 10 8"><path d="M1 6l4-4 4 4" stroke="#fff" stroke-width="1.6" fill="none"/></svg></div>

</body>
</html>
```